Small but growing painting company. Have built up a steady client base. Want to start having a more professional look. Want to start with changing my business cards, and also getting new logo and tee shirts.

Target Market(s)

Home owners, property management companies, all ages 30-70

Industry/Entity Type

Painting And Decorating

Contact Information for Business Card

Bright Ridge Painting LLC Mark Delvecchi 630-584-3907 interior, exterior, vaulted ceiling, drywall repair, pressure washing, kitchen cabinets, epoxy, garage floors,

Font styles to use
Sans Serif
Other font styles liked:
• Harrington

Colors
0355a3
ffffff
ec1f27
000000
3176b5
0493ce
474747
b7b7b7

Requirements
Must have
• Creative, something that doesn’t look like every other painting card.
Nice to have
• I would like something with an arrow or something going to a point

```html
<!DOCTYPE html>
<html lang="en">
<head>
<meta charset="utf-8">
<title>Bright Ridge Painting LLC – Business Card</title>
<link href="https://fonts.googleapis.com/css2?family=Montserrat:wght@500;700;800&display=swap" rel="stylesheet">
<style>
  :root {
    --stage: #1b1b1b;
    --card-white: #ffffff;
    --card-black: #0c0c0c;
    --red: #ec1f27;
    --blue: #0493ce;
    --orange: #f57c1f;
    --yellow: #ffe600;
    --text-light: #ffffff;
    --rule: #b7b7b7;
  }
  * { margin: 0; padding: 0; box-sizing: border-box; }
  html, body { width: 1200px; height: 1200px; overflow: hidden; }
  body {
    background: var(--stage);
    font-family: "Montserrat", sans-serif;
    display: flex;
    flex-direction: column;
    align-items: center;
    justify-content: center;
    gap: 44px;
  }
  .card {
    width: 900px;
    height: 514px;
    border-radius: 26px;
    position: relative;
    overflow: hidden;
  }
  .card-front { background: var(--card-white); }
  .card-back { background: var(--card-black); color: var(--text-light); }

  .brand {
    display: flex;
    align-items: center;
    gap: 22px;
  }
  .brand-mark {
    border-radius: 50%;
    border: 7px solid var(--blue);
    flex: none;
  }
  .brand-name {
    font-weight: 800;
    color: var(--red);
    text-transform: uppercase;
    line-height: 1.05;
  }
  .card-front .brand {
    position: absolute;
    left: 50%; top: 50%;
    transform: translate(-50%, -50%);
  }
  .card-front .brand-mark { width: 130px; height: 130px; }
  .card-front .brand-name { font-size: 40px; }

  .card-back .brand { position: absolute; left: 56px; top: 56px; }
  .card-back .brand-mark { width: 150px; height: 150px; border-width: 8px; }
  .card-back .brand-name { font-size: 46px; }

  .person {
    position: absolute;
    left: 60px; top: 300px;
    width: 360px;
    font-size: 28px;
    font-weight: 700;
    text-transform: uppercase;
    padding-bottom: 12px;
    border-bottom: 2px solid var(--rule);
  }
  .contact {
    position: absolute;
    right: 56px; top: 296px;
    width: 380px;
    text-align: right;
    font-size: 22px;
    font-weight: 500;
    padding-bottom: 12px;
    border-bottom: 2px solid var(--rule);
  }
  .contact-line {
    display: flex;
    justify-content: flex-end;
    align-items: center;
    gap: 12px;
    margin-bottom: 6px;
  }
  .contact-line svg { width: 20px; height: 20px; }

  .services {
    position: absolute;
    left: 60px; right: 56px; top: 392px;
    display: flex;
    justify-content: space-between;
    list-style: none;
  }
  .service-group li {
    display: flex;
    align-items: center;
    gap: 10px;
    font-size: 22px;
    font-weight: 500;
    line-height: 1.45;
  }
  .service-group svg { width: 16px; height: 16px; flex: none; }

  .accent-band {
    position: absolute;
    left: 0; right: 0; bottom: 0;
    height: 14px;
    background: linear-gradient(90deg, var(--red), var(--orange) 45%, var(--yellow));
  }
</style>
</head>
<body>

  <section class="card card-front" aria-label="Card front">
    <div class="brand">
      <span class="brand-mark"></span>
      <span class="brand-name">Bright Ridge<br>Painting LLC</span>
    </div>
  </section>

  <section class="card card-back" aria-label="Card back">
    <svg width="0" height="0" style="position:absolute">
      <defs>
        <linearGradient id="point-grad" x1="0" y1="0" x2="1" y2="0">
          <stop offset="0" stop-color="#ec1f27"/>
          <stop offset="1" stop-color="#ffe600"/>
        </linearGradient>
        <symbol id="point" viewBox="0 0 16 16">
          <path d="M2 2 L14 8 L2 14 L5 8 Z" fill="url(#point-grad)"/>
        </symbol>
      </defs>
    </svg>

    <div class="brand">
      <span class="brand-mark"></span>
      <span class="brand-name">Bright Ridge<br>Painting LLC</span>
    </div>

    <h1 class="person">Mark Delvecchi</h1>

    <div class="contact">
      <div class="contact-line">630-584-3907
        <svg viewBox="0 0 24 24"><path fill="#f57c1f" d="M6.6 10.8a15.1 15.1 0 0 0 6.6 6.6l2.2-2.2a1 1 0 0 1 1-.25 11.4 11.4 0 0 0 3.6.57 1 1 0 0 1 1 1V20a1 1 0 0 1-1 1A17 17 0 0 1 3 4a1 1 0 0 1 1-1h3.5a1 1 0 0 1 1 1c0 1.25.2 2.45.57 3.57a1 1 0 0 1-.25 1z"/></svg>
      </div>
      <div class="contact-line">info@brightridgepainting.com
        <svg viewBox="0 0 24 24"><rect x="2" y="5" width="20" height="14" rx="2" fill="#f57c1f"/><path d="M3 6l9 7 9-7" fill="none" stroke="#ec1f27" stroke-width="2"/></svg>
      </div>
    </div>

    <div class="services">
      <ul class="service-group">
        <li><svg><use href="#point"/></svg>Pressure washing</li>
        <li><svg><use href="#point"/></svg>Kitchen cabinets</li>
      </ul>
      <ul class="service-group">
        <li><svg><use href="#point"/></svg>Epoxy</li>
        <li><svg><use href="#point"/></svg>Garage floors</li>
      </ul>
      <ul class="service-group">
        <li><svg><use href="#point"/></svg>Interior</li>
        <li><svg><use href="#point"/></svg>Exterior</li>
      </ul>
      <ul class="service-group">
        <li><svg><use href="#point"/></svg>Vaulted ceiling</li>
        <li><svg><use href="#point"/></svg>Drywall repair</li>
      </ul>
    </div>

    <div class="accent-band"></div>
  </section>

</body>
</html>
```